Card design for Heating and Cooling company

this is for a heating and cooling company we recently updated our logo and need to update our cards. We attached our logo so you can incorporate it into the card. We specialize in residential and commercial furnace and air condition repairs. Have been in business since 2014.

Phone number 618.274.9031

We need the following phrases
:Repairs, Installations, and maintenance
:Quality work at reasonable prices
:residential/commercial
:Licensed &Insured
:Email Pinecresthvac47@mailbox-demo.com
Name: Tadeusz K (Ted)
Also on back side I would like my logo with wording :Thank you for your business and refferal

Industry/Entity Type

Hvac

Contact Information for Business Card

:residential/commercial
:Licensed & Insured
Name: Tadeusz K (Ted)
Number:618.274.9030

Requirements
Must have
• Blue and red colors
Nice to have
• Maybe a pic of a furnace or air conditioner

```html
<!DOCTYPE html>
<html lang="en">
<head>
<meta charset="UTF-8">
<title>Pinecrest Heating &amp; Cooling – Business Card</title>
<link href="https://fonts.googleapis.com/css2?family=Work+Sans:wght@400;500;700&display=swap" rel="stylesheet">
<style>
  :root {
    --page-bg: #111111;
    --card-bg: #1d1d1d;
    --card-edge: #262626;
    --silver: #d6d6d6;
    --text-light: #dcdcdc;
    --text-muted: #a8a8a8;
    --logo-deep: #3a3a3a;
    --divider: #4a4a4a;
    --heat-red: #d7322f;
    --cool-blue: #2f7fd6;
  }
  * { box-sizing: border-box; margin: 0; padding: 0; }
  html, body {
    width: 1200px;
    height: 900px;
    overflow: hidden;
    background: var(--page-bg);
    font-family: "Work Sans", Arial, sans-serif;
  }
  .canvas {
    width: 1200px;
    height: 900px;
    display: flex;
    flex-direction: column;
    align-items: center;
    justify-content: center;
    gap: 40px;
  }
  .card {
    position: relative;
    width: 700px;
    height: 400px;
    background: var(--card-bg);
    border: 1px solid var(--card-edge);
    overflow: hidden;
  }
  .accent-stripe {
    position: absolute;
    left: 0;
    right: 0;
    bottom: 0;
    height: 8px;
    display: flex;
  }
  .accent-stripe .stripe-heat { flex: 1; background: var(--heat-red); }
  .accent-stripe .stripe-cool { flex: 1; background: var(--cool-blue); }

  .brand-name {
    text-align: center;
    font-weight: 700;
    text-transform: uppercase;
    line-height: 1.1;
  }
  .brand-name .brand-main {
    display: block;
    font-size: 44px;
    letter-spacing: 1px;
  }
  .brand-name .brand-sub {
    display: block;
    font-size: 14px;
    letter-spacing: 5px;
    margin-top: 4px;
  }

  .card-front {
    display: flex;
    flex-direction: column;
    align-items: center;
    justify-content: center;
    padding-bottom: 8px;
  }
  .card-front .brand-name { color: var(--silver); }
  .rule-pair {
    display: flex;
    gap: 6px;
    margin: 22px 0 18px;
  }
  .rule-pair span { width: 40px; height: 3px; }
  .rule-pair .rule-heat { background: var(--heat-red); }
  .rule-pair .rule-cool { background: var(--cool-blue); }
  .service-list {
    list-style: none;
    text-align: center;
    color: var(--text-light);
    font-size: 16px;
    line-height: 26px;
  }
  .service-list .service-key { color: var(--cool-blue); font-weight: 500; }
  .thanks-line {
    margin-top: 18px;
    font-size: 15px;
    font-style: normal;
    color: var(--heat-red);
    font-weight: 500;
    letter-spacing: 0.5px;
  }

  .card-back {
    display: flex;
    align-items: center;
    padding-bottom: 8px;
  }
  .card-back .brand-block {
    width: 250px;
    display: flex;
    justify-content: center;
  }
  .card-back .brand-name { color: var(--logo-deep); }
  .card-back .brand-name .brand-main { font-size: 30px; }
  .card-back .brand-name .brand-sub { font-size: 10px; letter-spacing: 3px; }
  .divider {
    width: 1px;
    height: 200px;
    background: var(--divider);
  }
  .contact-block {
    padding-left: 40px;
    color: var(--text-light);
  }
  .person-name {
    font-size: 26px;
    font-weight: 500;
    letter-spacing: 1px;
  }
  .person-role {
    font-size: 16px;
    color: var(--heat-red);
    margin-top: 2px;
    margin-bottom: 8px;
  }
  .person-tags {
    font-size: 14px;
    color: var(--text-muted);
    margin-bottom: 18px;
  }
  .contact-list { list-style: none; }
  .contact-list li {
    display: flex;
    align-items: center;
    gap: 10px;
    font-size: 17px;
    line-height: 27px;
    letter-spacing: 0.3px;
    white-space: nowrap;
  }
  .contact-list svg {
    width: 12px;
    height: 12px;
    flex: none;
    stroke: var(--cool-blue);
    fill: none;
    stroke-width: 1.6;
  }
</style>
</head>
<body>
<main class="canvas">
  <section class="card card-front">
    <div class="brand-name">
      <span class="brand-main">Pinecrest</span>
      <span class="brand-sub">Heating &amp; Cooling</span>
    </div>
    <div class="rule-pair"><span class="rule-heat"></span><span class="rule-cool"></span></div>
    <ul class="service-list">
      <li><span class="service-key">Repairs, Installations, and Maintenance</span></li>
      <li>Quality work at reasonable prices</li>
      <li>Residential / Commercial &nbsp;•&nbsp; Licensed &amp; Insured</li>
    </ul>
    <p class="thanks-line">Thank you for your business and referral</p>
    <div class="accent-stripe"><span class="stripe-heat"></span><span class="stripe-cool"></span></div>
  </section>

  <section class="card card-back">
    <div class="brand-block">
      <div class="brand-name">
        <span class="brand-main">Pinecrest</span>
        <span class="brand-sub">Heating &amp; Cooling</span>
      </div>
    </div>
    <div class="divider"></div>
    <div class="contact-block">
      <h1 class="person-name">TADEUSZ K (TED)</h1>
      <p class="person-role">Director</p>
      <p class="person-tags">Residential / Commercial • Licensed &amp; Insured</p>
      <ul class="contact-list">
        <li>
          <svg viewBox="0 0 12 12"><path d="M3 1 L5 3 L4 4.5 Q5 7 7.5 8 L9 7 L11 9 L9.5 11 Q3 10 1 2.5 Z"/></svg>
          618.274.9031
        </li>
        <li>
          <svg viewBox="0 0 12 12"><rect x="3" y="1" width="6" height="10" rx="1"/><line x1="5.5" y1="9" x2="6.5" y2="9"/></svg>
          618.274.9030
        </li>
        <li>
          <svg viewBox="0 0 12 12"><rect x="1" y="2.5" width="10" height="7"/><polyline points="1,2.5 6,7 11,2.5"/></svg>
          Pinecresthvac47@mailbox-demo.com
        </li>
        <li>
          <svg viewBox="0 0 12 12"><circle cx="6" cy="6" r="5"/><ellipse cx="6" cy="6" rx="2" ry="5"/><line x1="1" y1="6" x2="11" y2="6"/></svg>
          www.Pinecresthvac-demo.com
        </li>
      </ul>
    </div>
    <div class="accent-stripe"><span class="stripe-heat"></span><span class="stripe-cool"></span></div>
  </section>
</main>
</body>
</html>
```